Broschüre für Gleichstellungsstelle einer kommunalen Stadtverwaltung
Sehr schönes und stimmiges Design, super schnelle Bearbeitung und zuvorkommende Kommunikation!
Zielgruppe
Wir sind die Gleichstellungsstelle einer kommunalen Stadtverwaltung (Einwohner*innen ca. 74.500) und richten uns mit unserer Arbeit grundsätzlich an alle Menschen.
Wir wollen eine Broschüre zum Handlungsleitfaden für die geschlechtergerechte Sprache bei der Stadt erstellen. Dieser soll an die Beschäftigten als Unterstützung verteilt werden.
Aufgabenstellung
- Broschüre mit Wire-O-Bindung, Druckformat 14,8 cm x 14,8 cm, Endformat 15,0 x 15,0 cm
- Spiralbindung an der Kopfseite
- doppelseitiges Deckblatt und Rückseite
- 16 Seiten Inhalt, wobei lediglich die Vorderseiten Text enthalten
- Schriftart (optimal Avenir Next, alternativ Arial) und Farbschema laut Corporate Design
- Der Text ist vorgegeben, die Gestaltung ist im Rahmen des Corporate Designs frei
Es soll eine ansprechende Broschüre gestaltet werden, welche die Leser*innen zum Blättern einlädt. Das bedeutet, dass alle Seiten (Deckblatt, Inhaltsseiten und Rückseiten) bei der Gestaltung berücksichtigt werden müssen.
Am Ende soll neben den üblichen Dateien auch eine fertige Druckdatei (siehe Datenblatt) zur Verfügung gestellt werden. Dabei ist zu beachten, dass die Spiralbindung des fertigen Produkts an der Kopfseite sein soll.

```html
<!DOCTYPE html>
<html lang="de">
<head>
<meta charset="utf-8">
<title>Pluralformen – Leitfaden geschlechtergerechte Sprache</title>
<link rel="stylesheet" href="https://fonts.googleapis.com/css2?family=Nunito+Sans:wght@300;400;700;800&display=swap">
<style>
  :root {
    --brand-green: #00504a;
    --text-grey: #5a5a5a;
    --tip-accent: #b3c8c1;
    --paper: #ffffff;
    --edge: #cfcfcf;
  }
  * { margin: 0; padding: 0; box-sizing: border-box; }
  html, body { width: 1200px; height: 1200px; overflow: hidden; background: var(--paper); }
  body { font-family: "Nunito Sans", "Avenir Next", Arial, sans-serif; }

  .page {
    position: relative;
    width: 1200px;
    height: 1200px;
    background: var(--paper);
    border: 1px solid var(--edge);
  }

  .intro-band {
    position: absolute;
    left: 0; top: 0;
    width: 100%;
    height: 383px;
    background: var(--brand-green);
    color: #fff;
    padding: 128px 0 0 81px;
  }
  .intro-title {
    font-size: 36px;
    font-weight: 800;
    letter-spacing: 0.2px;
    line-height: 1.15;
    margin-bottom: 8px;
  }
  .intro-text {
    font-size: 27px;
    font-weight: 400;
    line-height: 40px;
  }

  .comparison {
    position: absolute;
    top: 447px;
    left: 81px;
    display: flex;
  }
  .comparison-column { width: 543px; }
  .comparison-heading {
    font-size: 34px;
    font-weight: 800;
    color: var(--brand-green);
    line-height: 40px;
    margin-bottom: 6px;
  }
  .comparison-list {
    list-style: none;
    font-size: 27px;
    font-weight: 300;
    color: var(--text-grey);
    line-height: 42px;
  }

  .tip-box {
    position: absolute;
    left: 0; top: 797px;
    width: 1078px;
    height: 243px;
    background: var(--brand-green);
  }
  .tip-mark {
    position: absolute;
    left: 49px; top: 28px;
  }
  .tip-content {
    position: absolute;
    left: 120px; top: 18px;
    color: #fff;
  }
  .tip-text {
    font-size: 30px;
    font-weight: 400;
    line-height: 41px;
  }
  .tip-swaps {
    list-style: none;
    margin-top: 10px;
    font-size: 30px;
    font-weight: 700;
    color: var(--tip-accent);
    line-height: 39px;
  }
</style>
</head>
<body>
<main class="page">
  <section class="intro-band">
    <h1 class="intro-title">PLURALFORMEN</h1>
    <p class="intro-text">Wenn es der Inhalt zulässt, bietet die Verwendung von Pluralformen<br>die Möglichkeit, alle Geschlechter einzubeziehen.<br>Zum Beispiel</p>
  </section>

  <section class="comparison">
    <div class="comparison-column">
      <h2 class="comparison-heading">statt:</h2>
      <ul class="comparison-list">
        <li>Der Fraktionsvorsitzende</li>
        <li>Der Beauftragte</li>
        <li>Der Sachverständige</li>
        <li>Jeder Jugendliche, der …</li>
        <li>Jeder Ehrenamtliche, der …</li>
      </ul>
    </div>
    <div class="comparison-column">
      <h2 class="comparison-heading">besser:</h2>
      <ul class="comparison-list">
        <li>Die Fraktionsvorsitzenden</li>
        <li>Die Beauftragten</li>
        <li>Die Sachverständigen</li>
        <li>Alle Jugendlichen, die …</li>
        <li>Alle Ehrenamtlichen, die …</li>
      </ul>
    </div>
  </section>

  <aside class="tip-box">
    <svg class="tip-mark" width="42" height="164" viewBox="0 0 42 164" aria-hidden="true">
      <rect x="1" y="0" width="38" height="106" fill="#fff"/>
      <circle cx="20" cy="142" r="21" fill="#fff"/>
    </svg>
    <div class="tip-content">
      <p class="tip-text">Tipp: Pronomen werden häufig in der männlichen Form<br>verwendet. Hierfür gibt es kleine,unkomplizierte Lösungen.</p>
      <ul class="tip-swaps">
        <li>jeder » alle</li>
        <li>keiner » niemand</li>
      </ul>
    </div>
  </aside>
</main>
</body>
</html>
```